" Empresa multidisciplinar, focada na reabilitação de pacientes com dor crônica, pós-operatório, reabilitação músculo esquelética em geral. Atendimento com educador físico, fisioterapeuta, médicos "

```html
<!DOCTYPE html>
<html lang="pt-BR">
<head>
<meta charset="UTF-8">
<title>Movara – Pasta institucional</title>
<link href="https://fonts.googleapis.com/css2?family=Montserrat:wght@400;600;700;800&display=swap" rel="stylesheet">
<style>
  :root {
    --bg: #e9e9e9;
    --navy: #172a4a;
    --navy-dark: #12223d;
    --yellow: #fcc814;
    --white: #ffffff;
    --muted: #c9d1de;
  }
  * { margin: 0; padding: 0; box-sizing: border-box; }
  html, body {
    width: 1200px; height: 1200px; overflow: hidden;
    background: var(--bg);
    font-family: "Montserrat", sans-serif;
  }
  .folder {
    position: absolute; left: 168px; top: 211px;
    width: 864px; height: 893px;
  }
  .pocket {
    position: absolute; left: 0; top: 0;
    width: 432px; height: 893px;
  }
  .panel {
    position: absolute; top: 0; width: 432px; height: 749px;
    background: var(--navy);
  }
  .panel--back { left: 0; background: var(--navy-dark); }
  .panel--front { left: 432px; }

  .back-mark {
    position: absolute; left: 50%; top: 248px; transform: translateX(-50%);
    display: flex; flex-direction: column; align-items: center; gap: 14px;
  }
  .back-mark .dot {
    width: 92px; height: 92px; border-radius: 50%;
    border: 5px solid var(--yellow);
  }
  .back-mark .name {
    font-weight: 800; font-size: 20px; color: var(--yellow); letter-spacing: 0.5px;
  }

  .contact {
    position: absolute; left: 30px; right: 20px; top: 572px;
    display: flex; align-items: flex-start; gap: 22px;
    color: var(--muted); font-size: 8.5px; line-height: 1.5;
  }
  .contact-item { display: flex; align-items: flex-start; gap: 6px; }
  .contact-item svg { flex: none; width: 11px; height: 11px; }

  .front-brand {
    position: absolute; left: 84px; top: 270px;
    display: flex; align-items: center; gap: 12px;
  }
  .front-brand .dot {
    width: 64px; height: 64px; border-radius: 50%;
    border: 4px solid var(--yellow);
  }
  .front-brand .name {
    font-weight: 800; font-size: 44px; line-height: 1; color: var(--yellow);
  }
  .front-brand .tagline {
    margin-top: 6px; font-weight: 600; font-size: 7.6px;
    letter-spacing: 0.4px; color: var(--white);
  }
</style>
</head>
<body>
  <div class="folder">
    <svg class="pocket" viewBox="0 0 432 893" aria-hidden="true">
      <path d="M0 325 C40 330 70 400 110 470 C150 530 200 560 432 560 L432 893 L0 893 Z" fill="var(--yellow)"/>
    </svg>

    <section class="panel panel--back">
      <div class="back-mark">
        <span class="dot"></span>
        <span class="name">Movara</span>
      </div>
      <div class="contact">
        <div class="contact-item">
          <svg viewBox="0 0 24 24"><circle cx="12" cy="12" r="11" fill="var(--muted)"/><path d="M8 7c1 3 4 7 8 9l1.5-1.8-2.5-1.5-1 1c-1.5-.7-3-2.3-3.6-3.6l1-1L10 7z" fill="var(--navy-dark)"/></svg>
          <span>+55 (11) 4820-3175</span>
        </div>
        <div class="contact-item">
          <svg viewBox="0 0 24 24"><rect x="2" y="5" width="20" height="14" rx="2" fill="var(--muted)"/><path d="M3 6l9 7 9-7" stroke="var(--navy-dark)" stroke-width="2" fill="none"/></svg>
          <span>contato@movara.com.br</span>
        </div>
        <div class="contact-item">
          <svg viewBox="0 0 24 24"><path d="M12 2a7 7 0 0 0-7 7c0 5 7 13 7 13s7-8 7-13a7 7 0 0 0-7-7z" fill="var(--muted)"/><circle cx="12" cy="9" r="2.5" fill="var(--navy-dark)"/></svg>
          <span>Rua das Acácias, 482<br>Bairro Vila Serena<br>04512-090 - São Paulo / SP</span>
        </div>
      </div>
    </section>

    <section class="panel panel--front">
      <div class="front-brand">
        <span class="dot"></span>
        <div>
          <div class="name">Movara</div>
          <div class="tagline">CENTRO DE REABILITAÇÃO MUSCULOESQUELÉTICA</div>
        </div>
      </div>
    </section>
  </div>
</body>
</html>
```